Educational Flashcard Packaging Box Design

We are an educational resource provider in Australia. We have a new product launching for high school students, age 13-18. Thye are flashcards that help students with literacy. We need the box design that will store the cards when the students keep them in the bag at school. They need to be fun and colourful.
Our brand colours are
#06D8D8
#EF0081
#FFC904
#FF9900

The 36 flashcards all have a different colour to make up a rainbow. See the image of the flashcards attached.

The box template is uploaded in the files.
The box dimensions are 91 x 35 x 129mm.
Updates

I had a baby on the 2nd June and am in the hospital until the 8th June so I haven't been able to manage the project.

Target Market(s)

School students age 12 -18

Requirements
Must have
• Name of the product: Brightmark Mastery Flashcards
Fun and engaging design.
Bright colours.
Our logo - attached.
Text:
Get results you can be proud of.
36 flashcards + instructions
Increase key word knowledge and understanding.
(C) Harbourline Study Guild 2021
Newcastle, NSW, Australia.
hsguild.edu.au
Nice to have
• Instructions for the back of the box:
1. Box the key word in every question and check its meaning in the flashcards.
2. Write the meaning above the key word.
3. Use the key word metalanguage in your answer, e.g. describe; use the words characteristics and features in your answer. E.g. explain; use the words cause and effect in your answer and use linking words to demonstrate the relationships.
4. Be sure to add relevant example/s where possible

```html
<!DOCTYPE html>
<html lang="en">
<head>
<meta charset="utf-8">
<title>Brightmark Mastery Flashcards – Box Panels</title>
<link rel="stylesheet" href="https://fonts.googleapis.com/css2?family=Fredoka:wght@500;700&family=Baloo+2:wght@700;800&family=Lexend:wght@300;500;700&display=swap">
<style>
  :root {
    --bg: #e6e6e6;
    --orange-light: #ffc21a;
    --orange-deep: #ff9f00;
    --ink: #111111;
    --white: #ffffff;
    --blue: #1f6fc4;
    --blue-dark: #2a3db0;
    --teal: #0a9aa0;
    --green-card: #a6ff00;
    --purple-frame: #5b16f0;
    --lavender-card: #d5bdf5;
    --violet-card: #a845ee;
    --yellow-card: #fde36a;
    --orange-frame: #ff8a00;
  }
  * { box-sizing: border-box; margin: 0; padding: 0; }
  html, body { width: 1200px; height: 750px; overflow: hidden; background: var(--bg); }
  .canvas { position: relative; width: 1200px; height: 750px; }
  .abs { position: absolute; }

  .panel {
    position: absolute; overflow: hidden;
    background: radial-gradient(circle at 40% 35%, var(--orange-light), var(--orange-deep) 90%);
  }

  /* Top panel */
  .box-top { left: 336px; top: 30px; width: 381px; height: 147px; }
  .top-strip {
    position: absolute; left: 40px; top: 46px; width: 301px; height: 56px; background: var(--white);
    display: flex; align-items: center; justify-content: center; text-align: center;
    font-family: "Baloo 2", sans-serif; font-weight: 700; font-size: 15px; line-height: 1.1; color: var(--blue);
  }

  /* Side panel */
  .box-side { left: 717px; top: 177px; width: 147px; height: 540px; }
  .side-stack {
    position: absolute; left: 50%; top: 50%; width: 480px;
    transform: translate(-50%, -50%) rotate(-90deg);
    display: flex; flex-direction: column; align-items: center; gap: 8px;
  }
  .side-title {
    font-family: "Fredoka", sans-serif; font-weight: 700; font-size: 40px; color: var(--ink); white-space: nowrap; line-height: 1;
    text-shadow: 3px 0 0 var(--white), -3px 0 0 var(--white), 0 3px 0 var(--white), 0 -3px 0 var(--white),
                 2px 2px 0 var(--white), -2px -2px 0 var(--white), 2px -2px 0 var(--white), -2px 2px 0 var(--white);
  }
  .side-band {
    padding: 2px 26px; background: linear-gradient(90deg, var(--teal), var(--blue-dark));
    font-family: "Baloo 2", sans-serif; font-weight: 800; font-size: 28px; line-height: 1.2; color: var(--white);
  }

  /* Front panel */
  .box-front { left: 336px; top: 177px; width: 381px; height: 540px; }
  .front-art { position: absolute; left: 0; top: 0; width: 494px; height: 700px; transform: scale(0.7713); transform-origin: top left; }

  .tagline {
    left: 40px; top: 30px; transform: rotate(8deg); transform-origin: left top;
    font-family: "Baloo 2", sans-serif; font-weight: 800; font-size: 27px;
    color: var(--white); text-shadow: 2px 2px 0 var(--blue); white-space: nowrap;
  }

  .card { position: absolute; overflow: hidden; font-family: "Lexend", sans-serif; color: var(--ink); }
  .card-word { font-weight: 700; line-height: 1; white-space: nowrap; }
  .card-desc { font-weight: 300; line-height: 1.2; }
  .card-desc b { font-weight: 700; }
  .card-art { position: absolute; border-radius: 10px; }
  .card-brand { position: absolute; font-family: "Lexend", sans-serif; font-weight: 500; font-size: 5px; color: var(--ink); white-space: nowrap; }
  .bubble { position: absolute; background: var(--white); border-radius: 10px; font-size: 5px; font-weight: 500; padding: 3px 6px; line-height: 1.2; }

  .card-contrast { left: 14px; top: 145px; width: 210px; height: 150px; background: var(--green-card); transform: rotate(-17deg); }
  .card-contrast .card-word { position: absolute; left: 10px; top: 30px; font-size: 26px; }
  .card-contrast .card-desc { position: absolute; left: 12px; top: 64px; font-size: 8.5px; width: 100px; }
  .card-contrast .bubble { left: 14px; top: 100px; }
  .card-contrast .card-art { right: 8px; top: 62px; width: 60px; height: 80px; background: linear-gradient(160deg, #ffd21c, #f5f5ff 70%); }

  .card-explain {
    left: 150px; top: 132px; width: 190px; height: 140px; background: var(--white);
    border: 12px solid var(--purple-frame); border-radius: 4px; transform: rotate(38deg);
    display: flex; align-items: center; justify-content: center;
  }
  .card-explain .card-word { font-size: 32px; transform: translate(-18px, -6px); }

  .card-interpret { left: 292px; top: 218px; width: 172px; height: 150px; background: var(--lavender-card); transform: rotate(-17deg); }
  .card-interpret .card-word { position: absolute; left: 12px; top: 22px; font-size: 28px; }
  .card-interpret .card-desc { position: absolute; left: 14px; top: 58px; font-size: 8.5px; }
  .card-interpret .bubble { left: 12px; top: 80px; }
  .card-interpret .card-art { right: 8px; top: 78px; width: 56px; height: 64px; background: linear-gradient(160deg, #e04f8a, #6b4a3a 60%); }
  .card-interpret .card-brand { left: 12px; bottom: 12px; }

  .title {
    left: 0; width: 494px; top: 340px; text-align: center; transform: rotate(7deg);
    font-family: "Fredoka", sans-serif; font-weight: 700; font-size: 44px; color: var(--ink); white-space: nowrap;
    text-shadow: 3px 0 0 var(--white), -3px 0 0 var(--white), 0 3px 0 var(--white), 0 -3px 0 var(--white),
                 2px 2px 0 var(--white), -2px -2px 0 var(--white), 2px -2px 0 var(--white), -2px 2px 0 var(--white),
                 4px 5px 0 var(--ink);
  }
  .title-band {
    left: 100px; top: 408px; width: 240px; height: 58px; transform: rotate(6deg);
    background: linear-gradient(90deg, var(--teal), var(--blue-dark));
    display: flex; align-items: center; justify-content: center;
    font-family: "Baloo 2", sans-serif; font-weight: 800; font-size: 36px; color: var(--white);
  }

  .card-investigate { left: 16px; top: 478px; width: 150px; height: 125px; background: var(--violet-card); transform: rotate(-14deg); }
  .card-investigate .card-word { position: absolute; left: 8px; top: 16px; font-size: 19px; }
  .card-investigate .card-desc { position: absolute; left: 10px; top: 42px; font-size: 7.5px; width: 62px; }
  .card-investigate .card-art { right: 10px; top: 40px; width: 38px; height: 72px; background: linear-gradient(180deg, #d9e8ff, #f5b400); border-radius: 20px; }
  .card-investigate .card-brand { left: 10px; bottom: 8px; }

  .card-clarify { left: 148px; top: 486px; width: 165px; height: 140px; background: var(--yellow-card); transform: rotate(28deg); }
  .card-clarify .card-word { position: absolute; left: 12px; top: 18px; font-size: 24px; }
  .card-clarify .card-desc { position: absolute; left: 14px; top: 48px; font-size: 8.5px; }
  .card-clarify .card-art { right: 40px; bottom: 10px; width: 70px; height: 50px; background: linear-gradient(90deg, #b89a7e, #3d2aa8); }
  .card-clarify .card-brand { left: 14px; top: 72px; }

  .card-analyse {
    left: 336px; top: 478px; width: 135px; height: 180px; background: var(--white);
    border: 11px solid var(--orange-frame); border-radius: 4px; transform: rotate(-30deg);
    display: flex; align-items: center; justify-content: center;
  }
  .card-analyse .card-word { font-size: 26px; transform: rotate(58deg); }

  .brand-mark {
    left: 18px; top: 612px; width: 96px; display: flex; flex-direction: column; align-items: center; gap: 4px;
    font-family: "Fredoka", sans-serif; font-weight: 700; font-size: 11px; line-height: 1.1; color: var(--white); text-align: center;
  }
  .brand-square { width: 18px; height: 18px; border: 2px solid var(--white); }

  .banner {
    left: 150px; top: 584px; width: 270px; height: 46px; background: var(--white); transform: rotate(12deg);
    font-family: "Baloo 2", sans-serif; font-weight: 700; font-size: 14px; line-height: 1.05; color: var(--blue);
    display: flex; align-items: center; justify-content: center; text-align: center;
  }
  .card-count {
    left: 188px; top: 640px; transform: rotate(12deg); display: flex; align-items: center; gap: 6px;
    font-family: "Baloo 2", sans-serif; font-weight: 800; font-size: 14px; line-height: 1; color: var(--blue);
    text-shadow: 1px 1px 0 var(--white), -1px -1px 0 var(--white), 1px -1px 0 var(--white), -1px 1px 0 var(--white);
  }
</style>
</head>
<body>
<main class="canvas">
  <section class="panel box-top" aria-label="Box top panel">
    <p class="top-strip">Increase key word knowledge<br>and understanding.</p>
  </section>

  <section class="panel box-front" aria-label="Box front panel">
    <div class="front-art">
      <p class="abs tagline">Get results you can be proud of.</p>

      <div class="card card-contrast">
        <span class="card-word">Contrast</span>
        <p class="card-desc">Show how things are <b>different or opposite.</b></p>
        <span class="bubble">Cold is the opposite<br>of hot.</span>
        <div class="card-art" role="img" aria-label="Illustration of a snowman beside a bright sun"></div>
        <span class="card-brand" style="left:12px;bottom:8px;">Harbourline Study Guild</span>
      </div>

      <div class="card card-explain"><span class="card-word">Explain</span></div>

      <div class="card card-interpret">
        <span class="card-word">Interpret</span>
        <p class="card-desc">Draw <b>meaning</b> from.</p>
        <span class="bubble">The meaning of....</span>
        <div class="card-art" role="img" aria-label="Illustration of a sloth reading beside a stack of books"></div>
        <span class="card-brand">Harbourline Study Guild</span>
      </div>

      <h1 class="abs title">Brightmark Mastery</h1>
      <div class="abs title-band">Flashcards</div>

      <div class="card card-investigate">
        <span class="card-word">Investigate</span>
        <p class="card-desc"><b>Plan, inquire</b> into and <b>draw conclusions</b> about.</p>
        <div class="card-art" role="img" aria-label="Illustration of a magnifying glass"></div>
        <span class="card-brand">Harbourline Study Guild</span>
      </div>

      <div class="card card-clarify">
        <span class="card-word">Clarify</span>
        <p class="card-desc">Make <b>clear</b> or <b>plain.</b></p>
        <span class="card-brand">Harbourline Study Guild</span>
        <div class="card-art" role="img" aria-label="Illustration of a cat cleaning a window"></div>
      </div>

      <div class="card card-analyse"><span class="card-word">Analyse</span></div>

      <div class="abs brand-mark">
        <span class="brand-square"></span>
        <span>Harbourline Study Guild</span>
      </div>

      <p class="abs banner">Increase key word knowledge<br>and understanding.</p>

      <div class="abs card-count">
        <svg width="26" height="30" viewBox="0 0 26 30" aria-hidden="true">
          <rect x="8" y="1" width="15" height="23" rx="3" fill="#1f6fc4" stroke="#fff" stroke-width="2" transform="rotate(12 15 12)"/>
          <rect x="2" y="4" width="15" height="23" rx="3" fill="#1f6fc4" stroke="#fff" stroke-width="2" transform="rotate(-8 9 15)"/>
        </svg>
        <span>36 Flashcards<br>+ Instructions</span>
      </div>
    </div>
  </section>

  <section class="panel box-side" aria-label="Box side panel">
    <div class="side-stack">
      <span class="side-title">Brightmark Mastery</span>
      <span class="side-band">Flashcards</span>
    </div>
  </section>
</main>
</body>
</html>
```